Page lark & Glimmerly ad needed

I am in need of a simple static image ad to be used for Pagelark & Glimmerly. A photo of a nice roof on a nice house. "Instant Satellite Roof Estimates" "Your house, your time & instant estimate" . Our logo file is here: https://www.filquarry.com/scl/fo/t52wqpzx73hmbnvekcy8d/ZKqWT5PLmNdbX3HfGsYe8r2?rlkey=vn7cz2ktbw94pqdr6yjmfx4cs&dl=0

Multiple variations will be purchased.

```html
<!DOCTYPE html>
<html lang="en">
<head>
<meta charset="utf-8">
<title>Halvard Roofing – Instant Satellite Roof Estimates</title>
<link href="https://fonts.googleapis.com/css2?family=Arimo:wght@400;700&display=swap" rel="stylesheet">
<style>
  :root {
    --ink: #000000;
    --cream: #ebe3d4;
    --gold: #e8b857;
    --white: #ffffff;
    --navy: #1f2d44;
  }
  * { margin: 0; padding: 0; box-sizing: border-box; }
  html, body { width: 1199px; height: 1200px; overflow: hidden; }
  body { font-family: "Arimo", Arial, sans-serif; background: var(--cream); }
  .ad { position: relative; width: 1199px; height: 1200px; overflow: hidden; background: var(--cream); }
  .dark-panel { position: absolute; left: 0; top: 0; width: 640px; height: 1141px; }

  .brand {
    position: absolute; left: 0; width: 600px; top: 172px;
    text-align: center; color: var(--white);
    font-weight: 700; font-size: 40px; letter-spacing: 3px; line-height: 1.1;
  }

  .headline-box {
    position: absolute; left: 76px; top: 364px; width: 446px; height: 220px;
    background: var(--white); display: flex; flex-direction: column;
    justify-content: center; align-items: center;
  }
  .headline-box span {
    font-weight: 700; font-size: 70px; line-height: 84px; color: var(--ink); letter-spacing: 0.5px;
  }
  .headline-gold {
    position: absolute; left: 0; width: 600px; top: 592px; text-align: center;
    color: var(--gold); font-weight: 700; font-size: 70px; line-height: 82px;
  }
  .tagline {
    position: absolute; left: 0; width: 600px; top: 774px; text-align: center;
    color: var(--white); font-size: 26px;
  }
  .cta {
    position: absolute; left: 135px; top: 823px; width: 328px; height: 79px;
    border-radius: 40px; background: var(--white); color: var(--ink);
    display: flex; align-items: center; justify-content: center;
    font-weight: 700; font-size: 27px; letter-spacing: 0.5px;
  }
  .why-title {
    position: absolute; left: 0; width: 600px; top: 914px; text-align: center;
    color: var(--gold); font-weight: 700; font-size: 33px;
  }
  .benefits { position: absolute; left: 0; width: 600px; top: 960px; list-style: none; }
  .benefits li {
    display: flex; justify-content: center; align-items: center; gap: 20px;
    color: var(--white); font-size: 22px; height: 35.5px;
  }
  .benefits li::before {
    content: ""; width: 12px; height: 12px; border-radius: 50%; background: var(--gold);
  }

  .photo {
    position: absolute; border: 7px solid var(--white); border-radius: 18px;
    box-shadow: 0 8px 22px rgba(0,0,0,0.18);
  }
  .photo-main {
    left: 766px; top: 121px; width: 413px; height: 776px; transform: rotate(4.3deg);
    background: linear-gradient(180deg, #3f7fcb 0%, #2d72c0 40%, #d9c9a4 62%, #c9b08a 100%);
  }
  .photo-rafters {
    left: 654px; top: 580px; width: 199px; height: 351px; transform: rotate(11.5deg);
    background: linear-gradient(180deg, #6e93d6 0%, #c9b48e 45%, #7f7a74 100%);
  }
  .photo-aerial {
    left: 896px; top: 686px; width: 209px; height: 416px; transform: rotate(-6deg);
    background: linear-gradient(180deg, #b8ab93 0%, #cfae72 50%, #a89b86 100%);
  }

  .footer-bar {
    position: absolute; left: 0; top: 1141px; width: 1199px; height: 59px;
    background: var(--white); display: flex; align-items: center; justify-content: space-between;
    padding: 0 38px 0 36px; color: var(--navy); font-weight: 700; font-size: 20px;
  }
  .contact { display: flex; align-items: center; gap: 11px; }
  .contact svg { width: 24px; height: 24px; }
</style>
</head>
<body>
<div class="ad">
  <svg class="dark-panel" viewBox="0 0 640 1141" aria-hidden="true">
    <path d="M0 0 H599 C617 250 630 520 623 760 C618 920 610 1040 605 1141 H0 Z" fill="#000"/>
  </svg>

  <div class="brand">HALVARD<br>ROOFING</div>

  <div class="headline-box"><span>INSTANT</span><span>SATELLITE</span></div>
  <div class="headline-gold">ROOF<br>ESTIMATES</div>
  <p class="tagline">Your house, your time &amp; instant estimate</p>
  <div class="cta">GET STARTED</div>
  <h2 class="why-title">Why Choose Us</h2>
  <ul class="benefits">
    <li>Satellite Technology</li>
    <li>Instant Estimates</li>
    <li>No Site Visit Needed</li>
  </ul>

  <div class="photo photo-main" role="img" aria-label="Photo of new timber roof framing against a blue sky"></div>
  <div class="photo photo-rafters" role="img" aria-label="Photo of roofers working on battens of a pitched roof with a chimney"></div>
  <div class="photo photo-aerial" role="img" aria-label="Aerial photo of a house roof under construction"></div>

  <footer class="footer-bar">
    <div class="contact">
      <svg viewBox="0 0 24 24" aria-hidden="true"><circle cx="12" cy="12" r="10" fill="none" stroke="currentColor" stroke-width="2.4"/><path d="M6 7c3 1 4 3 3 5s1 4 3 5M14 4c0 3 2 4 4 4" fill="none" stroke="currentColor" stroke-width="2.4"/></svg>
      <span>halvardroofing.com</span>
    </div>
    <div class="contact">
      <svg viewBox="0 0 24 24" aria-hidden="true"><path d="M6.6 10.8a15.1 15.1 0 0 0 6.6 6.6l2.2-2.2c.3-.3.7-.4 1-.2 1.1.4 2.3.6 3.6.6.6 0 1 .4 1 1V20c0 .6-.4 1-1 1C10.6 21 3 13.4 3 4c0-.6.4-1 1-1h3.5c.6 0 1 .4 1 1 0 1.3.2 2.5.6 3.6.1.3 0 .7-.2 1L6.6 10.8z" fill="currentColor"/></svg>
      <span>(555) 014-2290</span>
    </div>
  </footer>
</div>
</body>
</html>
```